Brennick Holdings Business Cards

These are professional business cards that are for my family office.
Put fake emails and phone numbers as of now until I finalize those components. This family office controls my families investments, assets, and future. The cards should be professional.
..
.
.
.
I just uploaded another variation of a logo I would like to see as a business card to I am inbeteen which logo to use

Target Market(s)

business

Industry/Entity Type

business

Contact Information for Business Card

Professional, wealth related, finance related.

Requirements
Must have
• Logo

```html
<!DOCTYPE html>
<html lang="en">
<head>
<meta charset="utf-8">
<title>Brennick Holdings Business Cards</title>
<link rel="stylesheet" href="https://fonts.googleapis.com/css2?family=Cinzel:wght@500&family=Montserrat:wght@500;600&display=swap">
<style>
  :root {
    --backdrop: #3a3b3d;
    --navy: #1b1f2c;
    --paper: #ffffff;
    --silver: #b9bbbe;
    --silver-light: #e4e5e7;
    --ink-soft: #d9dadc;
    --divider: #4a4f5e;
  }
  * { box-sizing: border-box; margin: 0; padding: 0; }
  html, body { width: 1200px; height: 1200px; overflow: hidden; }
  body {
    background: var(--backdrop);
    position: relative;
    font-family: "Montserrat", Arial, sans-serif;
  }
  .card {
    position: absolute;
    left: 170px;
    width: 860px;
    height: 492px;
    border-radius: 40px;
    overflow: hidden;
  }
  .card-front { top: 90px; background: var(--navy); }
  .card-back { top: 618px; background: var(--navy); }

  .front-header {
    position: absolute; inset: 0 0 auto 0;
    height: 208px;
    background: var(--paper);
    display: flex; align-items: center; justify-content: center;
  }
  .silver-band {
    position: absolute; left: 0; right: 0; top: 208px; height: 14px;
    background: linear-gradient(90deg, var(--silver), var(--silver-light) 50%, var(--silver));
  }
  .company-name {
    font-family: "Cinzel", "Times New Roman", serif;
    font-weight: 500;
    letter-spacing: 2px;
    color: var(--navy);
    font-size: 58px;
  }
  .front-body {
    position: absolute; left: 0; right: 0; top: 222px; bottom: 0;
    display: flex; align-items: center;
  }
  .identity {
    width: 50%;
    padding-left: 60px;
  }
  .full-name {
    font-weight: 600; font-size: 40px; letter-spacing: 1px;
    color: var(--silver);
  }
  .job-title {
    font-weight: 500; font-size: 26px; color: var(--ink-soft);
    margin-top: 4px;
  }
  .divider {
    width: 1px; height: 170px; background: var(--divider);
  }
  .contacts {
    list-style: none;
    padding-left: 44px;
    display: flex; flex-direction: column; gap: 10px;
  }
  .contacts li {
    display: flex; align-items: center; gap: 12px;
    color: var(--ink-soft); font-size: 24px; font-weight: 500;
  }
  .contacts svg { width: 24px; height: 24px; flex: none; }

  .card-back {
    display: flex; flex-direction: column; align-items: center; justify-content: center; gap: 36px;
  }
  .brand-dot {
    width: 150px; height: 150px; border-radius: 50%;
    border: 5px solid var(--paper);
  }
  .card-back .company-name { color: var(--paper); font-size: 56px; }
</style>
</head>
<body>
  <section class="card card-front" aria-label="Business card front">
    <header class="front-header">
      <h1 class="company-name">Brennick Holdings</h1>
    </header>
    <div class="silver-band"></div>
    <div class="front-body">
      <div class="identity">
        <p class="full-name">FULL NAME</p>
        <p class="job-title">TITLE</p>
      </div>
      <div class="divider"></div>
      <ul class="contacts">
        <li>
          <svg viewBox="0 0 24 24" fill="#c4c6c9"><path d="M6.6 10.8a15 15 0 0 0 6.6 6.6l2.2-2.2a1 1 0 0 1 1-.25 11 11 0 0 0 3.6.6 1 1 0 0 1 1 1V20a1 1 0 0 1-1 1A17 17 0 0 1 3 4a1 1 0 0 1 1-1h3.5a1 1 0 0 1 1 1c0 1.25.2 2.45.6 3.6a1 1 0 0 1-.25 1z"/></svg>
          (000) 000 0000
        </li>
        <li>
          <svg viewBox="0 0 24 24" fill="none" stroke="#c4c6c9" stroke-width="1.8"><rect x="7" y="2" width="10" height="20" rx="2"/><line x1="11" y1="18.5" x2="13" y2="18.5"/></svg>
          (000) 000 0000
        </li>
        <li>
          <svg viewBox="0 0 24 24" fill="none" stroke="#c4c6c9" stroke-width="1.8"><rect x="2" y="5" width="20" height="14" rx="1"/><path d="M2 6l10 7 10-7"/></svg>
          office@brennick-mail.com
        </li>
        <li>
          <svg viewBox="0 0 24 24" fill="none" stroke="#c4c6c9" stroke-width="1.6"><circle cx="12" cy="12" r="10"/><ellipse cx="12" cy="12" rx="4.5" ry="10"/><line x1="2" y1="12" x2="22" y2="12"/><line x1="4" y1="7" x2="20" y2="7"/><line x1="4" y1="17" x2="20" y2="17"/></svg>
          www.brennick-office.com
        </li>
      </ul>
    </div>
  </section>

  <section class="card card-back" aria-label="Business card back">
    <div class="brand-dot"></div>
    <h2 class="company-name">Brennick Holdings</h2>
  </section>
</body>
</html>
```